Stationery Required - Own Logo provided

Hi,

We are a retail company called 'Copperfinch Trading Limited' based in the UK and would like some corporate stationery designed.

We have provided our Logo which we would like to use (Its attached to this brief)...

The designs must be orginal, professional, stylish and interesting!

Target Market(s)

We will use this stationery to communicate with our wholesale suppliers and employees, so it must have a 'professional' feel about it.

Industry/Entity Type

It Company

Requirements
Must have
• Must be professional, corporate, stylish and not to 'fussy'. we require ... Business card design, a4 letter, compliment slip. All designs must be supplied in a format where the text (address/telephone numbers etc..) can be edited, as we have alot of staff and operate out of several different premises.
Nice to have
• I would like a windows backround picture file supplied as well so we can integrate that onto our computer systems.

```html
<!DOCTYPE html>
<html lang="en">
<head>
<meta charset="utf-8">
<title>Copperfinch Trading Limited – Stationery Set</title>
<link rel="stylesheet" href="https://fonts.googleapis.com/css2?family=Didact+Gothic&family=Arimo:ital,wght@0,400;1,700&display=swap">
<style>
  :root {
    --green-dark: #3f5d1f;
    --green-light: #8cc63e;
    --sheet-edge: #b9b9b9;
    --paper: #ffffff;
    --text-soft: #4d6a2c;
  }
  * { box-sizing: border-box; margin: 0; padding: 0; }
  html, body { width: 1200px; height: 900px; overflow: hidden; background: var(--paper); }
  .canvas { position: relative; width: 1200px; height: 900px; }

  .sheet { position: absolute; background: var(--paper); border: 1px solid var(--sheet-edge); overflow: hidden; }
  .band { position: absolute; }
  .band--dark { background: var(--green-dark); }
  .band--light { background: var(--green-light); }

  .brand { position: absolute; display: flex; align-items: center; gap: 8px; color: var(--green-dark); font-family: "Didact Gothic", sans-serif; }
  .brand__mark { background: var(--green-dark); flex: none; }
  .brand__text { display: flex; flex-direction: column; line-height: 1; }
  .brand__name { letter-spacing: -0.5px; }
  .brand__sub { letter-spacing: 0.45em; margin-top: 4px; }

  .divider { position: absolute; width: 1.5px; background: var(--green-dark); }

  .contact { position: absolute; font-family: "Arimo", sans-serif; font-style: italic; font-weight: 700; color: var(--green-dark); font-size: 9.5px; line-height: 14px; }
  .contact--right { text-align: right; }

  .person__name { position: absolute; font-family: "Arimo", sans-serif; color: var(--green-dark); font-size: 34px; font-weight: 400; }
  .person__role { position: absolute; font-family: "Arimo", sans-serif; color: var(--green-dark); font-size: 15px; }

  .web-strip { position: absolute; display: flex; align-items: center; justify-content: space-between; padding: 0 14px; background: var(--green-light); color: var(--paper); font-family: "Arimo", sans-serif; font-size: 11px; letter-spacing: 1px; }

  .greeting { position: absolute; font-family: "Arimo", sans-serif; font-style: italic; color: var(--text-soft); font-size: 33px; }
</style>
</head>
<body>
<main class="canvas">

  <!-- Letterhead -->
  <section class="sheet letterhead" style="left:36px; top:68px; width:558px; height:760px;">
    <div class="band band--dark" style="left:0; top:0; width:300px; height:12px;"></div>
    <div class="band band--dark" style="left:0; top:0; width:14px; height:150px;"></div>
    <div class="band band--light" style="left:212px; bottom:0; width:346px; height:16px;"></div>
    <div class="band band--light" style="right:0; top:632px; width:20px; height:128px;"></div>

    <div class="brand" style="left:54px; top:50px;">
      <span class="brand__mark" style="width:34px; height:34px;"></span>
      <span class="brand__text">
        <span class="brand__name" style="font-size:31px;">Copperfinch</span>
        <span class="brand__sub" style="font-size:10px;">TRADING LIMITED</span>
      </span>
    </div>
    <div class="divider" style="left:290px; top:52px; height:56px;"></div>
    <address class="contact contact--right" style="right:18px; top:50px; width:250px;">
      Tel: 07700 900418<br>
      email copperfinch@mailhub.co.uk<br>
      The company registered office address is 17 mill<br>
      lane, Ardmore, County Down BT30 2LQ
    </address>
  </section>

  <!-- Business card, front -->
  <section class="sheet card card--front" style="left:696px; top:66px; width:416px; height:230px;">
    <div class="band band--dark" style="left:28px; top:0; width:60px; height:58px;"></div>
    <div class="band band--dark" style="left:88px; top:58px; width:36px; height:36px;"></div>
    <div class="brand" style="left:34px; top:100px; gap:12px;">
      <span class="brand__mark" style="width:54px; height:54px;"></span>
      <span class="brand__text">
        <span class="brand__name" style="font-size:46px;">Copperfinch</span>
        <span class="brand__sub" style="font-size:13px;">TRADING LIMITED</span>
      </span>
    </div>
  </section>

  <!-- Business card, back -->
  <section class="sheet card card--back" style="left:694px; top:368px; width:420px; height:232px;">
    <div class="brand" style="right:16px; top:10px; gap:6px;">
      <span class="brand__mark" style="width:24px; height:24px;"></span>
      <span class="brand__text">
        <span class="brand__name" style="font-size:22px;">Copperfinch</span>
        <span class="brand__sub" style="font-size:7px; margin-top:2px;">TRADING LIMITED</span>
      </span>
    </div>
    <div class="band band--dark" style="right:0; top:64px; width:236px; height:4px;"></div>
    <h1 class="person__name" style="left:18px; top:78px;">Martin Keane</h1>
    <p class="person__role" style="left:66px; top:120px;">Company Director</p>
    <address class="contact contact--right" style="right:10px; top:140px; width:260px; font-size:9px; line-height:13px;">
      Tel: 07700 900418<br>
      email copperfinch@mailhub.co.uk<br>
      The company registered office address is 17 mill<br>
      lane, Ardmore, County Down BT30 2LQ
    </address>
    <div class="web-strip" style="left:0; bottom:0; width:100%; height:16px;">
      <span>w</span><span>w</span><span>w</span><span>.</span><span>c</span><span>o</span><span>p</span><span>p</span><span>e</span><span>r</span><span>f</span><span>i</span><span>n</span><span>c</span><span>h</span><span>.</span><span>c</span><span>o</span><span>.</span><span>u</span><span>k</span>
    </div>
  </section>

  <!-- Compliment slip -->
  <section class="sheet comp-slip" style="left:614px; top:636px; width:556px; height:224px;">
    <div class="band band--dark" style="right:0; top:0; width:36px; height:100%;"></div>
    <div class="brand" style="left:16px; top:14px;">
      <span class="brand__mark" style="width:32px; height:32px;"></span>
      <span class="brand__text">
        <span class="brand__name" style="font-size:29px;">Copperfinch</span>
        <span class="brand__sub" style="font-size:9px;">TRADING LIMITED</span>
      </span>
    </div>
    <div class="divider" style="left:232px; top:16px; height:50px;"></div>
    <address class="contact" style="left:240px; top:12px; width:260px; font-style:normal; font-weight:400; font-size:9px; line-height:13px;">
      Tel: 07700 900418<br>
      email copperfinch@mailhub.co.uk<br>
      The company registered office address is 17 mill<br>
      lane, Ardmore, County Down BT30 2LQ
    </address>
    <p class="greeting" style="left:22px; top:136px;">With compliments....</p>
  </section>

</main>
</body>
</html>
```